KALVENTA Branded Wellness Pouch Design for Clinical Study Kit

Overview:
We are creating custom zippered pouches for our “KALVENTA Trial Spark Packs,” which will be distributed to physicians, nurses, and research coordinators participating in a national clinical study. We need a clean, professional design for the front of the pouch that incorporates our existing KALVENTA logo and the new supporting text.
Design Requirements:
Keep the existing KALVENTA logo intact (we’ll upload the file).
Add the text “Trial Spark Pack” immediately following the logo, using the same or a complementary font.
Add a tagline below that reads:
Recharge. Kalventa. Rise.
Use a layout that looks balanced, legible, and polished when printed on a small pouch.
Stay consistent with our brand color palette (blue from the logo)
The overall style should feel modern, wellness-driven, and professional — think premium, science-forward, and sleek.
Audience:
This kit will be given to medical professionals, so the design should feel elevated and credible (not flashy or overly playful).
Deliverables:
Vector file (AI, EPS)
It is a frosted white, zippered vinyl pouch (9 1/2 " x 8 1/4 " x 2 1/2 ")
The imprint size is (6 3/4" W x 4 1/2" H)
The imprint can only be 1-color, so in this case - we would like the color to be the dark blue (#06173c)

```html
<!DOCTYPE html>
<html lang="en">
<head>
<meta charset="utf-8">
<title>KALVENTA Trial Spark Pack – Pouch Imprint</title>
<link href="https://fonts.googleapis.com/css2?family=Antonio:wght@700&family=Oswald:wght@400&family=League+Spartan:wght@800&display=swap" rel="stylesheet">
<style>
  :root {
    --ink: #272c6c;
    --paper: #ffffff;
    --frame: #ececec;
  }
  * { margin: 0; padding: 0; box-sizing: border-box; }
  html, body {
    width: 1200px;
    height: 1000px;
    overflow: hidden;
    background: var(--paper);
  }
  .canvas {
    position: relative;
    width: 1200px;
    height: 1000px;
    background: var(--paper);
  }
  .imprint-area {
    position: absolute;
    left: 109px;
    top: 186px;
    width: 976px;
    height: 651px;
    border: 1px solid var(--frame);
  }
  .brand-mark {
    position: absolute;
    left: 124px;
    top: 396px;
    width: 40px;
    height: 40px;
    background: var(--ink);
  }
  .brand-name {
    position: absolute;
    left: 218px;
    top: 347px;
    font-family: "Oswald", "Arial Narrow", sans-serif;
    font-weight: 400;
    font-size: 124px;
    line-height: 1;
    letter-spacing: 1px;
    color: var(--ink);
    white-space: nowrap;
  }
  .study-line {
    position: absolute;
    left: 222px;
    top: 474px;
    width: 546px;
    font-family: "Oswald", "Arial Narrow", sans-serif;
    font-weight: 400;
    font-size: 15px;
    line-height: 1.2;
    color: var(--ink);
    white-space: nowrap;
    text-align: justify;
    text-align-last: justify;
  }
  .divider {
    position: absolute;
    left: 800px;
    top: 365px;
    width: 3px;
    height: 126px;
    background: var(--ink);
  }
  .kit-name {
    position: absolute;
    left: 835px;
    top: 362px;
    width: 236px;
    font-family: "Antonio", "Arial Narrow", sans-serif;
    font-weight: 700;
    font-size: 52px;
    line-height: 1.2;
    color: var(--ink);
    text-transform: uppercase;
    white-space: nowrap;
  }
  .tagline-band {
    position: absolute;
    left: 122px;
    top: 541px;
    width: 948px;
    height: 75px;
    background: var(--ink);
    display: flex;
    align-items: center;
    justify-content: center;
  }
  .tagline {
    font-family: "League Spartan", "Futura", sans-serif;
    font-weight: 800;
    font-size: 54px;
    line-height: 1;
    letter-spacing: 3px;
    color: var(--paper);
    text-transform: uppercase;
    padding-top: 6px;
    white-space: nowrap;
  }
</style>
</head>
<body>
  <main class="canvas">
    <section class="imprint-area" aria-label="Pouch imprint area"></section>
    <div class="brand-mark" aria-hidden="true"></div>
    <h1 class="brand-name">KALVENTA</h1>
    <p class="study-line">NUVRA Graft Randomized, Sham-Controlled, Multi-Center, Double Blind Clinical Trial</p>
    <div class="divider" aria-hidden="true"></div>
    <p class="kit-name">Trial<br>Spark Pack</p>
    <div class="tagline-band">
      <p class="tagline">Recharge. Kalventa. Rise.</p>
    </div>
  </main>
</body>
</html>
```